I need the following on my business card:
- Name: Dana Whitcomb
- License # 0M93216
- Title: Producer
- Phone: (555) 017-3904
- Email: Dana@CorbelInsuranceServices.com

- Company: Corbel Insurance Services
- Address: 27408 Larkmoor Ave Suite 610, Alder Glen, NV 90217
- Website: www.CorbelInsuranceServices.com

Also add our slogan on the card: "Where Trust Meets Coverage"

```html
<!DOCTYPE html>
<html lang="en">
<head>
<meta charset="utf-8">
<title>Corbel Insurance Services — Business Card</title>
<link rel="stylesheet" href="https://fonts.googleapis.com/css2?family=Poppins:wght@400;500;600&display=swap">
<style>
  :root {
    --navy: #23336f;
    --green: #139a48;
    --grey: #6f6f6f;
    --paper: #ffffff;
    --backdrop: #e9e9e9;
  }
  * { margin: 0; padding: 0; box-sizing: border-box; }
  html, body { width: 1200px; height: 2345px; overflow: hidden; }
  body {
    background: var(--backdrop);
    font-family: "Poppins", sans-serif;
    position: relative;
  }
  .card {
    position: absolute;
    left: 209px;
    width: 782px;
    height: 447px;
    background: var(--paper);
    box-shadow: 0 18px 30px -18px rgba(0,0,0,0.35);
    overflow: hidden;
  }
  .card--front { top: 1242px; }
  .card--back { top: 1722px; }

  /* Front */
  .wordmark {
    position: absolute;
    left: 0; right: 0;
    top: 172px;
    text-align: center;
    color: var(--navy);
    font-weight: 600;
  }
  .wordmark__name {
    display: inline-flex;
    align-items: center;
    gap: 18px;
    font-size: 66px;
    line-height: 1;
    letter-spacing: 1px;
  }
  .wordmark__square { width: 40px; height: 40px; background: var(--green); }
  .wordmark__sub {
    display: block;
    margin-top: 18px;
    font-size: 25px;
    line-height: 1;
    letter-spacing: 8px;
  }
  .slogan {
    position: absolute;
    left: 0; right: 0;
    top: 378px;
    text-align: center;
    color: var(--navy);
    font-weight: 600;
    font-size: 19px;
    line-height: 24px;
    letter-spacing: 5px;
  }

  /* Back */
  .person { position: absolute; left: 58px; top: 59px; }
  .person__name { color: var(--navy); font-weight: 500; font-size: 44px; line-height: 1.15; }
  .person__title { color: var(--grey); font-size: 26px; line-height: 1.2; margin-left: 4px; }

  .contacts { position: absolute; left: 60px; top: 185px; list-style: none; }
  .contacts li { display: flex; align-items: center; height: 43px; color: var(--navy); font-weight: 500; font-size: 19.5px; }
  .contacts svg { width: 32px; height: 32px; margin-right: 14px; flex: none; }

  .license { position: absolute; left: 60px; top: 390px; color: var(--grey); font-size: 15px; line-height: 20px; letter-spacing: 0.5px; }

  .wordmark--small { top: 36px; left: auto; right: 55px; text-align: left; }
  .wordmark--small .wordmark__name { font-size: 34px; gap: 10px; }
  .wordmark--small .wordmark__square { width: 20px; height: 20px; }
  .wordmark--small .wordmark__sub { font-size: 13.5px; letter-spacing: 4.3px; margin-top: 10px; }

  .corner-art { position: absolute; right: 0; bottom: 0; width: 465px; height: 290px; }
  .address {
    position: absolute;
    left: 465px; top: 370px;
    color: var(--paper);
    font-size: 18.5px;
    line-height: 1.2;
    letter-spacing: 0.4px;
  }
</style>
</head>
<body>

<section class="card card--front" aria-label="Card front">
  <div class="wordmark">
    <span class="wordmark__name"><span class="wordmark__square"></span>CORBEL</span>
    <span class="wordmark__sub">INSURANCE SERVICES</span>
  </div>
  <p class="slogan">WHERE TRUST MEETS COVERAGE</p>
</section>

<section class="card card--back" aria-label="Card back">
  <div class="person">
    <h1 class="person__name">Dana Whitcomb</h1>
    <p class="person__title">Producer</p>
  </div>

  <ul class="contacts">
    <li>
      <svg viewBox="0 0 32 32" aria-hidden="true"><circle cx="16" cy="16" r="16" fill="var(--green)"/><path d="M11 9.5l3 .2 1.2 3.4-1.8 1.3a9 9 0 0 0 4.2 4.2l1.3-1.8 3.4 1.2.2 3c-.2.9-1 1.5-2 1.5C14.3 22.3 9.7 17.7 9.5 11.5c0-1 .6-1.8 1.5-2z" fill="#fff"/></svg>
      (555) 017-3904
    </li>
    <li>
      <svg viewBox="0 0 32 32" aria-hidden="true"><circle cx="16" cy="16" r="16" fill="var(--green)"/><rect x="8.5" y="11" width="15" height="10.5" rx="1.2" fill="#fff"/><path d="M8.8 11.6l7.2 5.4 7.2-5.4" fill="none" stroke="var(--green)" stroke-width="1.4"/></svg>
      Dana@CorbelInsuranceServices.com
    </li>
    <li>
      <svg viewBox="0 0 32 32" aria-hidden="true"><circle cx="16" cy="16" r="16" fill="var(--green)"/><g fill="none" stroke="#fff" stroke-width="1.5"><circle cx="16" cy="16" r="7.5"/><ellipse cx="16" cy="16" rx="3.2" ry="7.5"/><path d="M8.5 16h15M9.6 12.2h12.8M9.6 19.8h12.8"/></g></svg>
      www.CorbelInsuranceServices.com
    </li>
  </ul>

  <p class="license">LICENSE #0M93216</p>

  <div class="wordmark wordmark--small">
    <span class="wordmark__name"><span class="wordmark__square"></span>CORBEL</span>
    <span class="wordmark__sub">INSURANCE SERVICES</span>
  </div>

  <svg class="corner-art" viewBox="0 0 465 290" role="img" aria-label="Mountain landscape decoration in green and navy">
    <polygon points="70,290 465,0 465,290" fill="var(--green)"/>
    <polygon points="0,290 465,40 465,290" fill="var(--navy)"/>
  </svg>

  <p class="address">27408 Larkmoor Ave Suite 610,<br>Alder Glen, NV 90217</p>
</section>

</body>
</html>
```